Business Card for Orthopaedic Clinic.
Should have nice design, double sided that includes logo
Should include my name, my contact, my email, webpage. A QR code to scan business card.

please use dummy information for privacy reasons. I will provide my name, email, practice address once a winner is selected.

Target Market(s)

Future patients

Contact Information for Business Card

Name: Dr Ruk
Contact No: +65 90417263
Practice Address: Singapore
Email: doctor@brevlo.com
Website: www.brevlo.com

Colors
00a990

Requirements
Must have
• Logo and a nice colour scheme.
A QR Code for Contact Card.
Name
Contact
Practice Address
Email
Website.
Nice to have
• Nice colour scheme
Should not have
• Nothing too cluttered.

```html
<!DOCTYPE html>
<html lang="en">
<head>
<meta charset="utf-8">
<title>Stride Orthopaedics – Business Card</title>
<link href="https://fonts.googleapis.com/css2?family=Montserrat:wght@400;500;700&display=swap" rel="stylesheet">
<style>
  :root {
    --teal: #43a19c;
    --teal-deep: #2f8c87;
    --teal-light: #52aea9;
    --ink: #4a5058;
    --rule: #b9bcc0;
    --paper-top: #ffffff;
    --paper-bottom: #e9eaec;
    --backdrop: #eceeef;
    --white: #ffffff;
  }
  * { box-sizing: border-box; margin: 0; padding: 0; }
  html, body { width: 1200px; height: 900px; overflow: hidden; }
  body {
    background: var(--backdrop);
    font-family: "Montserrat", sans-serif;
    display: flex;
    flex-direction: column;
    align-items: center;
    justify-content: center;
    gap: 50px;
  }
  .card {
    position: relative;
    width: 665px;
    height: 380px;
    border-radius: 4px;
    overflow: hidden;
    box-shadow: 0 6px 18px rgba(0,0,0,0.12);
  }

  /* Front */
  .card-front {
    background: linear-gradient(160deg, var(--paper-top) 0%, var(--paper-bottom) 100%);
  }
  .brand {
    position: absolute;
    left: 42px;
    top: 48px;
    display: flex;
    align-items: center;
    gap: 16px;
  }
  .brand-mark {
    width: 52px;
    height: 52px;
    border-radius: 8px;
    background: var(--teal);
  }
  .brand-name {
    font-weight: 500;
    font-size: 21px;
    letter-spacing: 3px;
    text-transform: uppercase;
    color: var(--ink);
  }
  .rule {
    position: absolute;
    height: 1px;
    background: var(--rule);
  }
  .rule-left { left: 52px; top: 150px; width: 355px; }
  .rule-right { left: 540px; top: 132px; width: 90px; }
  .person {
    position: absolute;
    left: 418px;
    top: 114px;
  }
  .person-name {
    font-size: 24px;
    font-weight: 400;
    letter-spacing: 1.5px;
    color: var(--ink);
  }
  .person-role {
    margin-top: 6px;
    margin-left: 10px;
    font-size: 13px;
    font-weight: 700;
    letter-spacing: 0.5px;
    color: var(--teal);
  }
  .contact-list {
    position: absolute;
    left: 52px;
    top: 198px;
    list-style: none;
  }
  .contact-item {
    display: flex;
    align-items: center;
    gap: 22px;
    height: 33px;
    font-size: 15px;
    letter-spacing: 1.8px;
    color: var(--ink);
  }
  .contact-icon {
    width: 26px;
    height: 26px;
    border-radius: 6px;
    background: var(--teal);
    display: flex;
    align-items: center;
    justify-content: center;
  }
  .contact-icon svg { width: 15px; height: 15px; }
  .front-band {
    position: absolute;
    left: 0; right: 0; bottom: 0;
    height: 26px;
    background: var(--teal-light);
  }

  /* Back */
  .card-back {
    background: linear-gradient(120deg, var(--teal-light) 0%, var(--teal) 55%, var(--teal-deep) 100%);
    display: flex;
    align-items: center;
    justify-content: center;
    gap: 24px;
  }
  .card-back .brand-mark {
    width: 86px;
    height: 86px;
    border-radius: 10px;
    background: var(--white);
  }
  .card-back .brand-name {
    color: var(--white);
    font-size: 30px;
    letter-spacing: 4px;
  }
</style>
</head>
<body>

<section class="card card-front" aria-label="Business card front">
  <div class="brand">
    <div class="brand-mark"></div>
    <span class="brand-name">Stride Orthopaedics</span>
  </div>

  <div class="rule rule-left"></div>
  <div class="person">
    <p class="person-name">Dr Ruk</p>
    <p class="person-role">SPECIALIST</p>
  </div>
  <div class="rule rule-right"></div>

  <ul class="contact-list">
    <li class="contact-item">
      <span class="contact-icon">
        <svg viewBox="0 0 24 24" fill="#fff"><path d="M6.6 10.8a15.1 15.1 0 0 0 6.6 6.6l2.2-2.2a1 1 0 0 1 1-.25 11.4 11.4 0 0 0 3.6.57 1 1 0 0 1 1 1V20a1 1 0 0 1-1 1A17 17 0 0 1 3 4a1 1 0 0 1 1-1h3.5a1 1 0 0 1 1 1c0 1.25.2 2.45.57 3.57a1 1 0 0 1-.25 1z"/></svg>
      </span>
      +65 90417263
    </li>
    <li class="contact-item">
      <span class="contact-icon">
        <svg viewBox="0 0 24 24" fill="#fff"><path d="M12 2a7 7 0 0 0-7 7c0 5.2 7 13 7 13s7-7.8 7-13a7 7 0 0 0-7-7zm0 9.5A2.5 2.5 0 1 1 12 6.5a2.5 2.5 0 0 1 0 5z"/></svg>
      </span>
      B-118, Kallang Road 12
    </li>
    <li class="contact-item">
      <span class="contact-icon">
        <svg viewBox="0 0 24 24" fill="none" stroke="#fff" stroke-width="2"><rect x="3" y="5" width="18" height="14" rx="1"/><path d="M3 6l9 7 9-7"/></svg>
      </span>
      doctor@brevlo.com
    </li>
    <li class="contact-item">
      <span class="contact-icon">
        <svg viewBox="0 0 24 24" fill="none" stroke="#fff" stroke-width="1.8"><circle cx="12" cy="12" r="9"/><path d="M3 12h18M12 3c3 3.2 3 14.8 0 18M12 3c-3 3.2-3 14.8 0 18"/></svg>
      </span>
      www.brevlo.com
    </li>
  </ul>

  <div class="front-band"></div>
</section>

<section class="card card-back" aria-label="Business card back">
  <div class="brand-mark"></div>
  <span class="brand-name">Stride Orthopaedics</span>
</section>

</body>
</html>
```